A new company focused on starting and investing in transformative businesses.

We need a simple and clean website with a few pages. we like larkmeadow.com as a starting point. we want the landing page to be very simple with an option to click through on the top right into INVESTOR LOGIN. then we want to be able to scroll down to see more about our company.

Target Market(s)

professional

Coding

Coded - Design and coding required

Number of Pages Required

2 page

Font styles to use
Serif
Sans Serif

Requirements
Must have
• HALVERN BUILDERS logo (attached as a file) on the top with INVESTOR LOGIN as a click through on the right. Please model the click through from larkmeadow.com. The description (also written in attached file) should be on the landing page. we do not want to have to scroll to read the description.

Then we can scroll down to read more about Halvern including the mission and the two types of businesses. More is detailed on the attached file called "Halvern Website Syntax"
Should not have
• should not be slow loading with lots of fancy graphics. should not be busy and with too many colors.

```html
<!DOCTYPE html>
<html lang="en">
<head>
<meta charset="utf-8">
<title>Halvern Builders</title>
<link href="https://fonts.googleapis.com/css2?family=Mulish:wght@400;600&family=Gelasio:wght@400;700&display=swap" rel="stylesheet">
<style>
:root{
  --blue:#135c9f;
  --blue-deep:#0e5aa0;
  --hero-bg:#f1f3f8;
  --text:#3a3a3a;
  --white:#ffffff;
  --pale:#cfe0f4;
}
*{margin:0;padding:0;box-sizing:border-box}
html,body{width:868px;height:1200px;overflow:hidden;background:var(--white)}
.page{position:relative;width:868px;height:1200px;font-family:"Gelasio",serif;color:var(--text)}
.hero{position:absolute;left:0;top:0;width:868px;height:372px;background:var(--hero-bg);overflow:hidden}
.hero-pattern{position:absolute;left:546px;top:0;width:322px;height:372px;
  background:linear-gradient(100deg,rgba(207,224,244,0) 0%,rgba(207,224,244,.7) 35%,var(--pale) 70%,#dbe8f7 100%)}
.brand{position:absolute;left:72px;top:18px;display:flex;align-items:center;gap:8px}
.brand-mark{width:30px;height:30px;background:var(--blue)}
.brand-name{font-family:"Mulish",sans-serif;font-size:15.5px;line-height:19px;color:#1f2a3a;letter-spacing:.5px}
.investor-login{position:absolute;right:74px;top:29px;font-family:"Mulish",sans-serif;font-size:14px;color:var(--blue);text-decoration:none}
.hero-title{position:absolute;left:72px;top:136px;width:400px;font-family:"Mulish",sans-serif;font-weight:400;font-size:20.5px;line-height:33px;color:var(--blue)}
.scroll-arrow{position:absolute;left:66px;top:313px}
.mission{position:absolute;left:72px;top:416px;width:379px;height:133px;background:var(--blue-deep);
  box-shadow:0 4px 14px rgba(0,0,0,.12);padding:7px 8px;color:var(--white);font-size:21.5px;line-height:29px}
.focus{position:absolute;left:483px;width:311px}
.focus h2{font-weight:400;font-size:20px;color:var(--blue);margin-bottom:6px}
.focus p{font-size:12px;line-height:20px;color:var(--text)}
.founder-photo{position:absolute;left:76px;top:746px}
.founders{position:absolute;left:292px;top:718px;width:510px}
.founders h2{font-weight:400;font-size:28px;color:var(--blue);margin-bottom:12px}
.founders h3{font-size:13px;color:var(--blue);margin-bottom:2px}
.founders p{font-size:12px;line-height:20px}
.team{position:absolute;left:0;top:902px;width:868px}
.member{position:absolute;width:110px;margin-left:-55px;text-align:center}
.member-name{font-family:"Mulish",sans-serif;font-size:10.5px;color:#222;margin-top:6px}
.member-name.active{color:var(--blue)}
.footer{position:absolute;left:0;top:1027px;width:868px;height:173px;background:var(--blue-deep);color:var(--white)}
.footer-company{position:absolute;left:73px;top:24px;font-size:13px;font-weight:700}
.footer-address{position:absolute;left:73px;top:52px;font-size:11.5px;line-height:18px}
.footer-media{position:absolute;left:598px;top:24px;font-size:11.5px;line-height:18px}
.footer-rule{position:absolute;left:70px;top:141px;width:729px;height:1px;background:rgba(255,255,255,.25)}
.copyright{position:absolute;left:0;top:152px;width:868px;text-align:center;font-size:11px}
</style>
</head>
<body>
<div class="page">
  <header class="hero">
    <div class="hero-pattern" role="img" aria-label="Soft pale blue geometric backdrop"></div>
    <div class="brand">
      <span class="brand-mark"></span>
      <span class="brand-name">HALVERN<br>BUILDERS</span>
    </div>
    <a class="investor-login" href="#">Investor Login</a>
    <h1 class="hero-title">Halvern Builders Is An Entrepreneurial Firm Focused On Building And Growing Transformational Companies</h1>
    <svg class="scroll-arrow" width="12" height="42" viewBox="0 0 12 42" aria-hidden="true">
      <line x1="6" y1="0" x2="6" y2="40" stroke="#135c9f" stroke-width="1"/>
      <polyline points="1,35 6,40 11,35" fill="none" stroke="#135c9f" stroke-width="1"/>
    </svg>
  </header>

  <section class="mission">Our mission is to build meaningful businesses that create enduring value by impacting people in a measurable way.</section>

  <section class="focus" style="top:420px">
    <h2>Ground Up</h2>
    <p>Our ground up business applies a proven analytic process to identify value edge, a form of competitive advantage. We architect transformational companies and are deliberate in creating the foundation necessary to lead an industry.</p>
  </section>
  <section class="focus" style="top:567px">
    <h2>Special Opportunities</h2>
    <p>We partner with exceptional teams that create value by transforming lives. Our investment focus includes large companies and spin-outs.</p>
  </section>

  <svg class="founder-photo" width="200" height="200" viewBox="0 0 200 200">
    <circle cx="96" cy="96" r="94" fill="none" stroke="#135c9f" stroke-width="1"/>
    <circle cx="96" cy="96" r="90" fill="#9aa6b4" role="img" aria-label="Portrait photo of the founder"/>
    <circle cx="165" cy="158" r="14" fill="#ffffff" stroke="#135c9f" stroke-width="1"/>
  </svg>

  <section class="founders">
    <h2>Halvern Builders</h2>
    <h3>Owen Calder Reyes</h3>
    <p>Lorem ipsum dolor sit amet, consectetuer adipiscing elit, sed diam nonuismod tincidunt ut leet dolore magna aliquam erat volutpat. Ut wisi enim ad minim veniam, quis nostrud exerci tation ullamcorper suscit lobortis nisl ut aliquip ex ea commodo consequat. Duis autem vel eum iriure dolor in hendrerit in vulputate velit ee molestie consequat.</p>
  </section>

  <div class="team">
    <div class="member" style="left:352px">
      <svg width="72" height="74" viewBox="0 0 72 74"><circle cx="36" cy="35" r="31" fill="#8f9caa" role="img" aria-label="Team member photo"/><path d="M3 34 A33 33 0 0 0 69 34" fill="none" stroke="#444" stroke-width="1"/><polygon points="33,68 39,68 36,71" fill="#444"/></svg>
      <div class="member-name active">Tobin Marsh</div>
    </div>
    <div class="member" style="left:464px">
      <svg width="72" height="74" viewBox="0 0 72 74"><circle cx="36" cy="35" r="31" fill="#9a9a9a" role="img" aria-label="Team member photo"/><path d="M3 34 A33 33 0 0 0 69 34" fill="none" stroke="#444" stroke-width="1"/><polygon points="33,68 39,68 36,71" fill="#444"/></svg>
      <div class="member-name">Wendell Ko</div>
    </div>
    <div class="member" style="left:565px">
      <svg width="72" height="74" viewBox="0 0 72 74"><circle cx="36" cy="35" r="31" fill="#4a4a4a" role="img" aria-label="Team member photo"/><path d="M3 34 A33 33 0 0 0 69 34" fill="none" stroke="#444" stroke-width="1"/><polygon points="33,68 39,68 36,71" fill="#444"/></svg>
      <div class="member-name">Curtis Vandamme</div>
    </div>
    <div class="member" style="left:673px">
      <svg width="72" height="74" viewBox="0 0 72 74"><circle cx="36" cy="35" r="31" fill="#5a5a5a" role="img" aria-label="Team member photo"/><path d="M3 34 A33 33 0 0 0 69 34" fill="none" stroke="#444" stroke-width="1"/><polygon points="33,68 39,68 36,71" fill="#444"/></svg>
      <div class="member-name">Lena Morrow,</div>
    </div>
  </div>

  <footer class="footer">
    <div class="footer-company">Halvern Builders Management, LLC</div>
    <div class="footer-address">218 Arden Lane, 9th Floor<br>Brookfield, NY 10402</div>
    <div class="footer-media">For media inquiries, please contact<br>press@halvernbuilders.com</div>
    <div class="footer-rule"></div>
    <div class="copyright">Copyright © 2021 Halvern Builders.&nbsp;&nbsp;All Right Reserved.</div>
  </footer>
</div>
</body>
</html>
```